Real estate company needs a letterhead design

A young real estate company needs a letterhead / stationery design, it should include the company's logo. It should look exactly the same as on the business cards. (With the phrase "a brand of KEV Wohnbau & Grundstücksentwicklung GmbH")

In addition, it should also include the 4 round seals.

color code blue # 00456b gray # 333333

Word and PDF are welcome.

KEV Wohnbau & Grundstücksentwicklung GmbH
Managing director: Mag. Lukas Fellnhuber
Matthias-Ortner-Strasse 3c / 41
6342 Lindenau

Tel .: +436648172093
Email: office@wohnglanz-beispiel.at
Web: www.wohnglanz-beispiel.at

Kreditkasse Almtal, Bergländer Kreditkasse from 1882, Genossenschaftskasse
Anton-Weissauer-Strasse 7, 6342 Lindenau
IBAN: AT31 4817 2964 0058 2316
BIC: GLMTAT44XXX
Account holder: KEV Wohnbau & Grundstücksentwicklung GmbH

FN: XXXXXXX
UID: XXXXXXX

```html
<!DOCTYPE html>
<html lang="de">
<head>
<meta charset="utf-8">
<title>Wohnglanz Letterhead</title>
<link rel="stylesheet" href="https://fonts.googleapis.com/css2?family=Karla:wght@400;700&display=swap">
<style>
  :root {
    --brand-blue: #00456b;
    --text-gray: #333333;
    --page-bg: #d4ebe4;
    --paper: #ffffff;
    --seal-red: #c8232c;
    --mark-tint: #e3e7ea;
  }
  html, body {
    margin: 0;
    padding: 0;
    width: 1200px;
    height: 1013px;
    overflow: hidden;
    background: var(--page-bg);
    font-family: "Karla", Arial, sans-serif;
  }
  .letterhead {
    position: absolute;
    left: 270px;
    top: 35px;
    width: 660px;
    height: 942px;
    background: var(--paper);
    box-shadow: 0 6px 24px rgba(0, 60, 50, 0.15);
    overflow: hidden;
  }
  .brand {
    position: absolute;
    left: 30px;
    top: 62px;
    display: flex;
    align-items: center;
    gap: 8px;
  }
  .brand-dot {
    width: 12px;
    height: 12px;
    background: var(--brand-blue);
    border-radius: 50%;
  }
  .brand-name {
    font-weight: 700;
    font-size: 30px;
    letter-spacing: 0.5px;
    color: var(--brand-blue);
  }
  .sender {
    position: absolute;
    left: 331px;
    top: 50px;
    width: 320px;
    font-size: 10px;
    line-height: 13px;
    color: var(--text-gray);
  }
  .sender p { margin: 0; white-space: nowrap; }
  .company { font-weight: 700; color: var(--brand-blue); }
  .label { color: var(--brand-blue); }
  .contact { margin-top: 5px !important; display: flex; gap: 12px; }
  .contact + .contact { margin-top: 2px !important; }
  .contact span { display: inline-flex; align-items: center; gap: 4px; }
  .contact svg { width: 9px; height: 9px; fill: var(--brand-blue); }
  .bank { margin-top: 5px !important; }
  .seals {
    position: absolute;
    left: 31px;
    top: 872px;
    display: flex;
    gap: 35px;
  }
  .seal {
    width: 30px;
    height: 30px;
    border: 2px solid var(--seal-red);
    border-radius: 50%;
    background: radial-gradient(circle, var(--seal-red) 0 9px, #fff 9.5px);
  }
  .mark-area {
    position: absolute;
    left: 291px;
    top: 748px;
    width: 354px;
    height: 194px;
    background: linear-gradient(180deg, rgba(227,231,234,0.3), var(--mark-tint));
  }
</style>
</head>
<body>
  <main class="letterhead">
    <div class="brand">
      <span class="brand-dot"></span>
      <span class="brand-name">WOHNGLANZ</span>
    </div>

    <section class="sender">
      <p class="company">KEV Wohnbau &amp; Grundstücksentwicklung GmbH</p>
      <p>Managing director: Mag. Lukas Fellnhuber</p>
      <p>Matthias-Ortner-Strasse 3c / 41</p>
      <p>6342 Lindenau</p>
      <p class="contact">
        <span><svg viewBox="0 0 10 10"><path d="M2 0.5 L3.8 2.6 L2.9 3.8 Q4 6 6.2 7.1 L7.4 6.2 L9.5 8 L8.4 9.5 Q1 8 0.5 1.6 Z"/></svg>+436648172093</span>
        <span><svg viewBox="0 0 10 10"><path d="M0.5 2 H9.5 V8 H0.5 Z M0.5 2 L5 5.5 L9.5 2" /></svg>office@wohnglanz-beispiel.at</span>
      </p>
      <p class="contact">
        <span><svg viewBox="0 0 10 10"><circle cx="5" cy="5" r="4.5"/></svg>www.wohnglanz-beispiel.at</span>
      </p>
      <p class="bank">Kreditkasse Almtal, Bergländer Kreditkasse from 1882,</p>
      <p>Genossenschaftskasse</p>
      <p>Anton-Weissauer-Strasse 7, 6342 Lindenau</p>
      <p><span class="label">IBAN:</span> AT31 4817 2964 0058 2316</p>
      <p><span class="label">BIC:</span> GLMTAT44XXX</p>
      <p><span class="label">Account holder:</span> KEV Wohnbau &amp; Grundstücksentwicklung GmbH</p>
      <p><span class="label">FN:</span> XXXXXXX</p>
      <p><span class="label">UID:</span> XXXXXXX</p>
    </section>

    <div class="seals">
      <span class="seal"></span>
      <span class="seal"></span>
      <span class="seal"></span>
      <span class="seal"></span>
    </div>

    <div class="mark-area" role="img" aria-label="Faint brand symbol watermark"></div>
  </main>
</body>
</html>
```